7KQ Pop Up Shop Clearance Flyer

We sell furniture. We opened up recently a temporary pop up shop to clear some stock we had from our old shop. So we don't have a full collection just our clearance lines that we want to get rid of - but the customer doesn't need to know this! Therefore the aim of this leaflet is to attract customers and make them come in - once they are there they might see something they like. As we will not be there for long - just a few more weeks.
We need a flyer to promote locally our pop up shop (temporary shop) with a Clearance Sale. The flyer will be sent by post or by hand to the local residents and by email to ex customers that bought from us before and we have their email address...
We need a modern fresh design flyer. At the next stage we will provide text for each item (brief description, dimensions and price) so allow some space for this.
Maybe we need to add a message or something to make people want to come quickly? For example most of the items are ex display or the last item and if they want it they should hurry as one is gone its gone. or you may have a better suggestion - let me know.
if you want to see some ideas of our website then 7KQ.co.uk

Target Market(s)

Local Residents around shop

Industry/Entity Type

Retail

Colors
0255a3
3176b5
85abd2

Requirements
Must have
• price tag showing RRP or WAS price and the Clearance Sale price
• Opening Hours: Mon-Fri 9:00am - 5:00pm, Sat: 9:00am - 4:00pm, Sun: Closed
• Tel: 0208 615 2973
• Shop Address: 142 Birchwood Row, Alder Vale, London, N21 7QD
Nice to have
• Parking behind Bo Pattersons
• Map of location

```html
<!DOCTYPE html>
<html lang="en">
<head>
<meta charset="utf-8">
<title>7KQ Furniture – Clearance Sale Flyer</title>
<link href="https://fonts.googleapis.com/css2?family=Bebas+Neue&family=Open+Sans:wght@400;600;700;800&family=Roboto:wght@700;900&display=swap" rel="stylesheet">
<style>
  :root{
    --brand-navy:#1f3a7a;
    --brand-blue:#1a67b5;
    --brand-mid:#3176b5;
    --brand-light:#85abd2;
    --ink:#1d2a44;
    --paper:#ffffff;
    --row-grey:#e6e7ea;
    --band-grey:#9c9ea3;
    --tag-red:#e3141b;
    --tag-black:#161616;
    --stage:#e4e4e4;
  }
  *{box-sizing:border-box;margin:0;padding:0}
  html,body{width:933px;height:1200px;overflow:hidden;background:var(--stage);font-family:"Open Sans",sans-serif;color:var(--ink)}
  .canvas{position:relative;width:933px;height:1200px}
  .spread{position:absolute;left:21px;width:891px;height:560px;display:grid;grid-template-columns:repeat(3,297px);background:var(--paper);box-shadow:0 6px 18px rgba(0,0,0,.18)}
  .spread--outside{top:20px}
  .spread--inside{top:620px}
  .panel{position:relative;overflow:hidden;height:560px}
  .photo{position:absolute}

  /* outside: about panel */
  .about{padding:34px 22px 0}
  .about h2,.hours h2{font-size:14px;font-weight:800;color:var(--brand-navy);letter-spacing:.3px;margin-bottom:6px}
  .about p{font-size:6.6px;line-height:1.45;margin-bottom:6px;color:#333}
  .hours{margin-top:12px}
  .hours h2{font-size:15px;color:var(--brand-blue)}
  .hours li{list-style:none;font-size:11px;font-weight:700;line-height:1.25}
  .about .photo{left:0;bottom:22px;width:297px;height:200px;background:linear-gradient(160deg,#c9cfd6,#8d96a1 55%,#6a6f76)}
  .about .foot-band{position:absolute;left:0;bottom:0;width:297px;height:50px}

  /* outside: contact panel */
  .contact{background:var(--brand-navy);color:#fff}
  .contact .photo{left:0;top:0;width:297px;height:150px;background:linear-gradient(170deg,#e9ecef,#a9b3c0 60%,#4a5c7a)}
  .contact .wave{position:absolute;left:0;top:120px;width:297px;height:40px}
  .map{position:absolute;left:58px;top:185px;width:180px;height:110px;background:linear-gradient(135deg,#f1f1f1,#dcdcdc)}
  .contact-info{position:absolute;left:20px;top:320px;right:20px}
  .contact-info h2{font-size:21px;font-weight:700;letter-spacing:.5px;text-align:center;margin-bottom:8px}
  .contact-info li{list-style:none;display:flex;gap:7px;align-items:center;font-size:12px;line-height:1.3;margin-bottom:5px;justify-content:center;text-align:center}
  .contact-info li.phone{font-size:15px;font-weight:700}
  .contact-info li svg{flex:none;width:11px;height:11px;fill:#fff}
  .parking{margin-top:8px;text-align:center;font-size:12px;font-weight:700}

  /* outside: cover panel */
  .cover{background:var(--paper)}
  .brand{position:absolute;top:26px;left:0;right:0;display:flex;flex-direction:column;align-items:center;gap:4px}
  .brand-mark{width:26px;height:26px;background:var(--brand-navy)}
  .brand-name{font-size:13px;font-weight:600;color:var(--ink);letter-spacing:.4px}
  .brand-sub{font-size:6px;color:#666;letter-spacing:.6px;text-transform:uppercase}
  .sale-band{position:absolute;top:98px;left:0;width:297px;height:36px;background:var(--brand-navy);color:#fff;font-family:"Bebas Neue",sans-serif;font-size:30px;line-height:38px;text-align:center;letter-spacing:1px}
  .cover .photo{left:0;top:134px;width:297px;height:200px;background:linear-gradient(160deg,#d8dde2,#b9a89a 55%,#8c6b66)}
  .cover-panel{position:absolute;left:0;top:305px;width:297px;height:255px}
  .cover-title{position:absolute;left:0;right:0;top:345px;text-align:center;color:#fff;font-family:"Bebas Neue",sans-serif;font-size:34px;line-height:.98;letter-spacing:.5px;font-weight:400}
  .cover-title span{display:block}
  .cover-title .small{font-size:28px}

  /* inside */
  .spread--inside .panel{background:#f7f7f7}
  .header-band{position:absolute;left:0;top:0;width:594px;height:80px;z-index:2}
  .header-title{position:absolute;left:30px;top:12px;z-index:3;font-family:"Open Sans",sans-serif;font-weight:800;font-size:32px;color:#fff;letter-spacing:.5px}
  .price{display:flex;flex-direction:column;align-items:center}
  .was{font-family:"Roboto",sans-serif;font-size:9px;font-weight:700;color:var(--tag-red);text-decoration:line-through;line-height:1.1}
  .tag{display:flex;align-items:center;background:var(--tag-black);border-radius:10px;height:18px;overflow:hidden;font-family:"Roboto",sans-serif}
  .tag .now{background:var(--tag-red);color:#fff;font-size:7px;font-weight:700;padding:0 5px;height:100%;line-height:18px;border-radius:10px}
  .tag .amount{color:#fff;font-size:14px;font-weight:900;padding:0 7px 0 4px}

  .sofa-list{position:absolute;left:14px;right:14px;top:86px;display:flex;flex-direction:column;gap:8px}
  .sofa{display:flex;align-items:center;justify-content:space-between;height:86px;background:var(--paper);border-bottom:5px solid var(--row-grey);padding:0 14px 0 8px}
  .sofa .thumb{width:140px;height:54px;background:linear-gradient(180deg,#9aa0a8,#5d6168)}
  .sofa .thumb.brown{background:linear-gradient(180deg,#8a6a55,#5a4538)}
  .sofa .thumb.dark{background:linear-gradient(180deg,#4a4c50,#1f2023)}
  .sofa .meta{display:flex;flex-direction:column;align-items:flex-end;gap:4px}
  .sofa .name{font-size:11px;font-weight:700;color:var(--brand-navy);text-align:right;line-height:1.15}

  .tile-grid{position:absolute;left:10px;right:10px;top:86px;bottom:10px;display:grid;grid-template-columns:1fr 1fr;grid-auto-rows:1fr;gap:8px}
  .tile,.chair{position:relative;background:var(--paper);border-bottom:4px solid var(--row-grey)}
  .tile .thumb{position:absolute;left:8px;right:8px;top:6px;bottom:38px;background:linear-gradient(160deg,#d9d2c6,#a89780)}
  .tile .thumb.white{background:linear-gradient(160deg,#f2f2f2,#d4d6d9)}
  .tile .thumb.green{background:linear-gradient(160deg,#3aa68f,#1c6f5e)}
  .tile .price,.chair .price{position:absolute;right:6px;bottom:4px}

  .chair-grid{position:absolute;left:10px;right:10px;top:12px;height:460px;display:grid;grid-template-columns:repeat(3,1fr);grid-template-rows:repeat(4,1fr);gap:8px}
  .chair .thumb{position:absolute;left:22px;right:22px;top:6px;bottom:38px;background:linear-gradient(180deg,#b9b6b1,#8b8884)}
  .chair .thumb.black{background:linear-gradient(180deg,#3a3a3a,#111)}
  .chair .thumb.white{background:linear-gradient(180deg,#f0f0f0,#cfcfcf)}
  .chair .thumb.appliance{left:30px;right:30px;background:linear-gradient(180deg,#eef2f6,#b6c6d8)}
  .chair .tag .amount{font-size:12px;padding:0 5px 0 3px}
  .chair .tag .now{font-size:6px;padding:0 4px}
  .hurry-band{position:absolute;left:0;bottom:0;width:297px;height:72px;background:var(--band-grey);color:#fff;font-family:"Open Sans",sans-serif;font-weight:800;font-size:17px;display:flex;align-items:center;justify-content:center;letter-spacing:.5px}
</style>
</head>
<body>
<main class="canvas">

  <section class="spread spread--outside">
    <article class="panel about">
      <h2>ABOUT US</h2>
      <p>7KQ Furniture has become one of the leading furniture suppliers to the property market within London. With over 15 years' experience, we have expanded and increased our business to supply not only Landlords and Managing Agents, but also Property Developers, Housing Associations and Local Councils.</p>
      <p>Our purpose is to provide a complete furniture solution according to your price level with just one call. You only have to place your order, tell us your requirements, and we provide a front start to finish service.</p>
      <p>Whatever you choose to buy, you can be sure of great value and high quality. We have no minimum order size and we will deliver, install and assemble all furniture, treating your property with care and respect.</p>
      <p>We deliver hundreds of in-stock items every day across London, offering a next-day delivery service on our regular stock range within the M25.</p>
      <div class="hours">
        <h2>OPENING HOURS</h2>
        <ul>
          <li>Mon-Fri 9:00am - 5:00pm</li>
          <li>Sat: 9:00am - 4:00pm</li>
          <li>Sun: Closed</li>
        </ul>
      </div>
      <div class="photo" role="img" aria-label="Bright open-plan living room with grey sofas, yellow cushions and a glass coffee table"></div>
      <svg class="foot-band" viewBox="0 0 297 50" preserveAspectRatio="none"><path d="M0 30 Q150 36 297 0 L297 50 L0 50Z" fill="var(--brand-blue)"/></svg>
    </article>

    <article class="panel contact">
      <div class="photo" role="img" aria-label="Grey fabric sofa bed with a blue throw in a modern flat"></div>
      <svg class="wave" viewBox="0 0 297 40" preserveAspectRatio="none"><path d="M0 40 Q120 36 297 0 L297 40Z" fill="var(--brand-navy)"/></svg>
      <div class="map" role="img" aria-label="Street map showing the shop location"></div>
      <div class="contact-info">
        <h2>CONTACT US</h2>
        <ul>
          <li class="phone"><svg viewBox="0 0 24 24"><path d="M6.6 10.8a15 15 0 0 0 6.6 6.6l2.2-2.2c.3-.3.7-.4 1-.2 1.1.4 2.3.6 3.6.6.6 0 1 .4 1 1V20c0 .6-.4 1-1 1A17 17 0 0 1 3 4c0-.6.4-1 1-1h3.5c.6 0 1 .4 1 1 0 1.3.2 2.5.6 3.6.1.3 0 .7-.2 1z"/></svg>0208 615 2973</li>
          <li><svg viewBox="0 0 24 24"><path d="M2 5h20v14H2zM2 5l10 8 10-8" stroke="var(--brand-navy)" stroke-width="1.5"/></svg>info@7kq.co.uk</li>
          <li><svg viewBox="0 0 24 24"><circle cx="12" cy="12" r="10"/></svg>7KQ.co.uk</li>
          <li><svg viewBox="0 0 24 24"><path d="M12 2a7 7 0 0 0-7 7c0 5 7 13 7 13s7-8 7-13a7 7 0 0 0-7-7zm0 9.5A2.5 2.5 0 1 1 12 6.5a2.5 2.5 0 0 1 0 5z"/></svg>142 Birchwood Row, Alder Vale, London, N21 7QD</li>
        </ul>
        <p class="parking">Parking behind Bo Pattersons</p>
      </div>
    </article>

    <article class="panel cover">
      <div class="brand">
        <span class="brand-mark"></span>
        <span class="brand-name">7KQ FURNITURE</span>
        <span class="brand-sub">Trade furniture solutions</span>
      </div>
      <div class="sale-band">CLEARANCE SALE</div>
      <div class="photo" role="img" aria-label="Modern bedroom with a light wood bed and city view"></div>
      <svg class="cover-panel" viewBox="0 0 297 255" preserveAspectRatio="none"><path d="M0 20 Q150 0 297 6 L297 255 L0 255Z" fill="var(--brand-blue)"/></svg>
      <h1 class="cover-title"><span class="small">COMPLETE RANGE OF</span><span>FURNITURE AND</span><span>APPLIANCES</span></h1>
    </article>
  </section>

  <section class="spread spread--inside">
    <svg class="header-band" viewBox="0 0 594 80" preserveAspectRatio="none"><path d="M0 10 Q300 0 594 0 L594 30 Q300 40 0 70Z" fill="var(--brand-blue)"/></svg>
    <h2 class="header-title">OUR PRODUCTS</h2>

    <article class="panel">
      <div class="sofa-list">
        <div class="sofa"><div class="thumb" role="img" aria-label="Grey sofa bed"></div><div class="meta"><span class="name">Lisbon</span><div class="price"><span class="was">£199</span><span class="tag"><span class="now">NOW</span><span class="amount">£89</span></span></div></div></div>
        <div class="sofa"><div class="thumb dark" role="img" aria-label="Dark grey corner sofa"></div><div class="meta"><span class="name">Tarra<br>corner sofa</span><div class="price"><span class="was">£199</span><span class="tag"><span class="now">NOW</span><span class="amount">£89</span></span></div></div></div>
        <div class="sofa"><div class="thumb brown" role="img" aria-label="Brown patterned sofabed"></div><div class="meta"><span class="name">Aurora<br>sofabed</span><div class="price"><span class="was">£199</span><span class="tag"><span class="now">NOW</span><span class="amount">£89</span></span></div></div></div>
        <div class="sofa"><div class="thumb" role="img" aria-label="Slim grey daybed sofa"></div><div class="meta"><span class="name">Verona</span><div class="price"><span class="was">£199</span><span class="tag"><span class="now">NOW</span><span class="amount">£89</span></span></div></div></div>
        <div class="sofa"><div class="thumb dark" role="img" aria-label="Black two-seater sofa"></div><div class="meta"><span class="name">Elmbay<br>2str</span><div class="price"><span class="was">£199</span><span class="tag"><span class="now">NOW</span><span class="amount">£89</span></span></div></div></div>
      </div>
    </article>

    <article class="panel">
      <div class="tile-grid">
        <div class="tile"><div class="thumb white" role="img" aria-label="Round dining table set"></div><div class="price"><span class="was">£199</span><span class="tag"><span class="now">NOW</span><span class="amount">£89</span></span></div></div>
        <div class="tile"><div class="thumb white" role="img" aria-label="Grey sofa bed"></div><div class="price"><span class="was">£199</span><span class="tag"><span class="now">NOW</span><span class="amount">£89</span></span></div></div>
        <div class="tile"><div class="thumb white" role="img" aria-label="Glass dining table with grey chairs"></div><div class="price"><span class="was">£199</span><span class="tag"><span class="now">NOW</span><span class="amount">£89</span></span></div></div>
        <div class="tile"><div class="thumb white" role="img" aria-label="White gloss desk"></div><div class="price"><span class="was">£199</span><span class="tag"><span class="now">NOW</span><span class="amount">£89</span></span></div></div>
        <div class="tile"><div class="thumb" role="img" aria-label="Wooden dining table and chairs"></div><div class="price"><span class="was">£199</span><span class="tag"><span class="now">NOW</span><span class="amount">£89</span></span></div></div>
        <div class="tile"><div class="thumb white" role="img" aria-label="Glass dining table"></div><div class="price"><span class="was">£199</span><span class="tag"><span class="now">NOW</span><span class="amount">£89</span></span></div></div>
        <div class="tile"><div class="thumb" role="img" aria-label="Wooden table with two chairs"></div><div class="price"><span class="was">£199</span><span class="tag"><span class="now">NOW</span><span class="amount">£89</span></span></div></div>
        <div class="tile"><div class="thumb white" role="img" aria-label="Glass coffee table"></div><div class="price"><span class="was">£199</span><span class="tag"><span class="now">NOW</span><span class="amount">£89</span></span></div></div>
        <div class="tile"><div class="thumb green" role="img" aria-label="Green curved sofa"></div><div class="price"><span class="was">£199</span><span class="tag"><span class="now">NOW</span><span class="amount">£89</span></span></div></div>
        <div class="tile"><div class="thumb white" role="img" aria-label="White gloss sideboard"></div><div class="price"><span class="was">£199</span><span class="tag"><span class="now">NOW</span><span class="amount">£89</span></span></div></div>
      </div>
    </article>

    <article class="panel">
      <div class="chair-grid">
        <div class="chair"><div class="thumb black" role="img" aria-label="Dark grey dining chair"></div><div class="price"><span class="was">£199</span><span class="tag"><span class="now">NOW</span><span class="amount">£89</span></span></div></div>
        <div class="chair"><div class="thumb" role="img" aria-label="Taupe dining chair"></div><div class="price"><span class="was">£199</span><span class="tag"><span class="now">NOW</span><span class="amount">£89</span></span></div></div>
        <div class="chair"><div class="thumb" role="img" aria-label="Light grey dining chair"></div><div class="price"><span class="was">£199</span><span class="tag"><span class="now">NOW</span><span class="amount">£89</span></span></div></div>
        <div class="chair"><div class="thumb" role="img" aria-label="Grey chair with chrome legs"></div><div class="price"><span class="was">£199</span><span class="tag"><span class="now">NOW</span><span class="amount">£89</span></span></div></div>
        <div class="chair"><div class="thumb white" role="img" aria-label="Light grey dining chair"></div><div class="price"><span class="was">£199</span><span class="tag"><span class="now">NOW</span><span class="amount">£89</span></span></div></div>
        <div class="chair"><div class="thumb black" role="img" aria-label="Black dining chair"></div><div class="price"><span class="was">£199</span><span class="tag"><span class="now">NOW</span><span class="amount">£89</span></span></div></div>
        <div class="chair"><div class="thumb black" role="img" aria-label="Black chair with chrome legs"></div><div class="price"><span class="was">£199</span><span class="tag"><span class="now">NOW</span><span class="amount">£89</span></span></div></div>
        <div class="chair"><div class="thumb black" role="img" aria-label="Black dining chair"></div><div class="price"><span class="was">£199</span><span class="tag"><span class="now">NOW</span><span class="amount">£89</span></span></div></div>
        <div class="chair"><div class="thumb white" role="img" aria-label="White chair with chrome legs"></div><div class="price"><span class="was">£199</span><span class="tag"><span class="now">NOW</span><span class="amount">£89</span></span></div></div>
        <div class="chair"><div class="thumb" role="img" aria-label="Grey dining chair"></div><div class="price"><span class="was">£199</span><span class="tag"><span class="now">NOW</span><span class="amount">£89</span></span></div></div>
        <div class="chair"><div class="thumb white" role="img" aria-label="White chair with chrome frame"></div><div class="price"><span class="was">£199</span><span class="tag"><span class="now">NOW</span><span class="amount">£89</span></span></div></div>
        <div class="chair"><div class="thumb appliance" role="img" aria-label="Water heater appliance"></div><div class="price"><span class="was">£199</span><span class="tag"><span class="now">NOW</span><span class="amount">£89</span></span></div></div>
      </div>
      <div class="hurry-band">LIMITED STOCK HURRY UP</div>
    </article>
  </section>

</main>
</body>
</html>
```